Real Estate Sign - For Sale Yard Sign - Bellwether Estates

Our real estate company is looking for a new sign design to hang from in post in the front yard of the homes we are selling. Our company name is Bellwether Estates and we are open to any ideas. Attached for you is our company logo and name. The font is Trajan Pro. We are looking for a classy sign to put in front of our high end more expensive homes. You can either choose to include or not include the words "FOR SALE" on the sign (in our state, only about 1/2 of the real estate signs have room for those words. It is implied with a sign in the yard in front of a home). Thank you.

24 inches wide is important. and the height should be either 18, 24 or 30 inches. For printing purposes either of those heights will work. 18 inches is common, but some signs look great that are taller too. I'm open.

If you have any ideas for some better text options, styles or fonts, feel free to play with it.

P.S. Please feel free to play with the colors. We are not at this point set on a particular color scheme. Colors we think are nice but you may have other better ideas are black, red, white, gold, green

Target Market(s)

High end real estate home owners who choose to use our company to sell their home.

Industry/Entity Type

Real Estate

Requirements
Must have
• Company Logo
Company Name (Bellwether Estates)
Thaddeus Vornholt (please include my name as I am the real estate agent)
503-618-2940 (my phone number for potential clients to contact me)
Website name - bellwetherestatesnw.example
***You can either choose to include the words "FOR SALE" or not***

Dimensions must be 24 inches wide. Height can be either 18, 24 or 30 inches. Must be one of those 3 heights for printing purposes.

```html
<!DOCTYPE html>
<html lang="en">
<head>
<meta charset="utf-8">
<title>18"h x 24"w Sign Design - Bellwether Estates Real Estate</title>
<link rel="stylesheet" href="https://fonts.googleapis.com/css2?family=Arimo:wght@400&family=Questrial&family=Roboto+Condensed:wght@300;400;700&display=swap">
<style>
  :root {
    --sheet-grey: #e6e6e6;
    --panel-white: #ffffff;
    --ink-black: #000000;
    --label-grey: #222222;
    --table-head: #454545;
    --sign-red: #ff0000;
    --sign-red-deep: #b80000;
    --sign-border: #b5b5b5;
    --rule-grey: #c8c8c8;
    --shadow: #000000;
  }
  * { box-sizing: border-box; margin: 0; padding: 0; }
  html, body { width: 1200px; height: 927px; overflow: hidden; background: var(--panel-white); }
  .sheet { position: relative; width: 1200px; height: 927px; background: var(--panel-white); }

  .sheet-header {
    position: absolute; left: 0; top: 0; width: 1200px; height: 43px;
    background: var(--sheet-grey);
    font-family: "Questrial", sans-serif; font-size: 24px; color: var(--ink-black);
    line-height: 43px; padding-left: 14px;
  }

  .sign {
    position: absolute; left: 163px; top: 88px; width: 873px; height: 654px;
    border: 1px solid var(--sign-border); background: var(--panel-white); overflow: hidden;
  }
  .sign-band { position: absolute; left: 0; top: 0; width: 873px; height: 654px; }

  .brand-name {
    position: absolute; left: 0; top: 92px; width: 873px; text-align: center;
    font-family: "Roboto Condensed", sans-serif; font-weight: 700; font-size: 84px;
    letter-spacing: 2px; color: var(--ink-black); line-height: 1;
  }

  .agent-name, .agent-phone {
    position: absolute; left: 0; width: 873px; text-align: center;
    font-family: "Roboto Condensed", sans-serif; color: var(--panel-white);
    text-shadow: 4px 4px 0 var(--shadow); line-height: 1; white-space: nowrap;
  }
  .agent-name { top: 332px; font-size: 86px; letter-spacing: 1px; }
  .agent-name .first { font-weight: 700; }
  .agent-name .last { font-weight: 400; }
  .agent-phone { top: 425px; font-size: 100px; font-weight: 700; letter-spacing: 2px; }

  .website {
    position: absolute; left: 0; top: 562px; width: 873px; text-align: center;
    font-family: "Roboto Condensed", sans-serif; font-size: 62px; color: var(--ink-black); line-height: 1;
  }
  .website .bold { font-weight: 700; }
  .website .light { font-weight: 300; }
  .website .regular { font-weight: 400; }

  .sheet-footer {
    position: absolute; left: 0; top: 770px; width: 1200px; height: 157px; background: var(--sheet-grey);
    font-family: "Arimo", sans-serif; font-size: 12px; color: var(--label-grey);
  }
  .info-box { position: absolute; top: 10px; height: 135px; background: var(--panel-white); border-radius: 10px; }
  .client-box { left: 72px; width: 210px; }
  .job-box { left: 389px; width: 191px; }
  .field { position: absolute; line-height: 14px; }
  .field .label { position: absolute; right: calc(100% + 8px); white-space: nowrap; text-align: right; }
  .field .value { white-space: nowrap; }

  .spec-table {
    position: absolute; left: 626px; top: 10px; width: 372px; height: 135px;
    background: var(--panel-white); border-radius: 10px; overflow: hidden;
  }
  .spec-head { height: 28px; background: var(--table-head); color: var(--panel-white); font-size: 12px; position: relative; }
  .spec-head span { position: absolute; top: 7px; }
  .spec-col-line { position: absolute; top: 28px; bottom: 0; width: 1px; background: var(--rule-grey); }
  .swatches { position: absolute; left: 7px; top: 36px; list-style: none; }
  .swatches li { height: 18px; display: flex; align-items: center; gap: 4px; }
  .chip { width: 11px; height: 11px; border-radius: 50%; border: 1px solid #444; display: inline-block; }
  .chip.black { background: var(--ink-black); }
  .chip.red { background: var(--sign-red); }
  .chip.gradient { background: radial-gradient(circle, var(--sign-red), var(--sign-red-deep)); }
  .chip.empty { background: var(--panel-white); }
  .spec-na { position: absolute; top: 36px; }
</style>
</head>
<body>
<div class="sheet">
  <header class="sheet-header">18"h x 24"w Sign Design - Bellwether Estates Real Estate</header>

  <section class="sign" aria-label="Yard sign, 18 by 24 inches">
    <svg class="sign-band" viewBox="0 0 873 654" width="873" height="654" aria-hidden="true">
      <defs>
        <radialGradient id="bandGradient" cx="0.5" cy="0.45" r="0.6">
          <stop offset="0" stop-color="#ff0000"/>
          <stop offset="0.55" stop-color="#e80000"/>
          <stop offset="1" stop-color="#b00000"/>
        </radialGradient>
      </defs>
      <path d="M0,256 C200,262 420,276 620,272 C720,270 800,262 873,258 L873,268 C800,272 720,280 620,282 C420,286 200,272 0,266 Z" fill="#000"/>
      <path d="M0,276 C200,282 420,296 620,292 C720,290 800,282 873,278 L873,544 L0,544 Z" fill="url(#bandGradient)"/>
    </svg>

    <p class="brand-name">BELLWETHER ESTATES</p>

    <p class="agent-name"><span class="first">THADDEUS</span> <span class="last">VORNHOLT</span></p>
    <p class="agent-phone">503.618.2940</p>
    <p class="website"><span class="bold">bellwether</span><span class="light">estates</span><span class="bold">nw</span><span class="regular">.example</span></p>
  </section>

  <footer class="sheet-footer">
    <div class="info-box client-box">
      <div class="field" style="left:5px; top:5px;"><span class="label">Client:</span><span class="value">Bellwether Estates Real Estate</span></div>
      <div class="field" style="left:5px; top:23px;"><span class="label">Address:</span><span class="value"></span></div>
      <div class="field" style="left:5px; top:94px;"><span class="label">Phone:</span><span class="value">503.618.2940</span></div>
      <div class="field" style="left:5px; top:112px;"><span class="label">Email:</span><span class="value"></span></div>
    </div>

    <div class="info-box job-box">
      <div class="field" style="left:4px; top:5px;"><span class="label">Contact:</span><span class="value"></span></div>
      <div class="field" style="left:4px; top:23px;"><span class="label">File:</span><span class="value">bellwether_18x24.pdf</span></div>
      <div class="field" style="left:4px; top:41px;"><span class="label">Revision:</span><span class="value">1</span></div>
      <div class="field" style="left:4px; top:59px;"><span class="label">Date:</span><span class="value">11/21/2013</span></div>
    </div>

    <div class="spec-table">
      <div class="spec-head">
        <span style="left:9px;">Colours / Pantones</span>
        <span style="left:143px;">Vinyl / Laminates</span>
        <span style="left:279px;">Substrates</span>
      </div>
      <span class="spec-col-line" style="left:130px;"></span>
      <span class="spec-col-line" style="left:256px;"></span>
      <ul class="swatches">
        <li><span class="chip black"></span>black</li>
        <li><span class="chip red"></span>red</li>
        <li><span class="chip gradient"></span>red gradient</li>
        <li><span class="chip empty"></span></li>
        <li><span class="chip empty"></span></li>
      </ul>
      <span class="spec-na" style="left:136px;">n/a</span>
      <span class="spec-na" style="left:262px;">n/a</span>
    </div>
  </footer>
</div>
</body>
</html>
```